Qamra
قمرة كافيه
Hello Designers:-
Please check your e-mail inbox.
Thank you so much!
plz star rating...
The front and the back of the card should be one color "Beige". In front, it only shows the logo, the address, e-mail, twitter and instagram accounts. No need to type any other word like the word "قمرة"
As for the back, we want a loyalty card with 6 stamps with "Qamra" shape drawing on each. and the 6th qamra has a FREE written on it (Pic provided in brief)
If you have any comments, questions or requirements please do not hesitate to contact me on my e-mail or here, in the discussion.
Thank you so much for your work! :)
Hello designers: Please make sure to read the project brief as we want a (Double) sided business card/loyalty card. Moreover, please be aware that the card color should follow the color of the store "Beige" and not the logo color (Store pic provided in the brief)
Thank you so much for your effort! And good luck!

```html
<!DOCTYPE html>
<html lang="en">
<head>
<meta charset="utf-8">
<title>Qamra – Business &amp; Loyalty Card</title>
<link rel="stylesheet" href="https://fonts.googleapis.com/css2?family=Amiri:wght@400;700&family=Arimo:wght@400;700&display=swap">
<style>
  :root {
    --stage: #d9d9d7;
    --beige-light: #ecd5ad;
    --beige: #dfc08f;
    --beige-deep: #cba676;
    --brown: #5a2c22;
    --brown-line: #7a4335;
    --gold: #e2c395;
  }
  * { box-sizing: border-box; margin: 0; padding: 0; }
  html, body { width: 1200px; height: 901px; overflow: hidden; }
  body {
    background: var(--stage);
    display: flex;
    align-items: center;
    justify-content: center;
    gap: 40px;
    font-family: "Arimo", Arial, sans-serif;
    color: var(--brown);
  }
  .card {
    position: relative;
    width: 540px;
    height: 309px;
    border-radius: 18px;
    overflow: hidden;
    background: linear-gradient(100deg, var(--beige-light) 0%, var(--beige) 45%, var(--beige-light) 70%, var(--beige-deep) 100%);
  }
  .card__frame {
    position: absolute;
    inset: 12px;
    border: 1.5px solid var(--brown-line);
    border-radius: 10px;
  }
  .card__corner {
    position: absolute;
    width: 46px; height: 46px;
    background: rgba(90,44,34,.16);
    border-radius: 6px;
  }
  .card__corner--tl { top: 18px; left: 18px; }
  .card__corner--tr { top: 18px; right: 18px; }
  .card__corner--bl { bottom: 18px; left: 18px; }
  .card__corner--br { bottom: 18px; right: 18px; }

  .brand {
    position: absolute;
    left: 0; right: 0;
    display: flex;
    align-items: center;
    justify-content: center;
    gap: 8px;
    font-weight: 700;
    line-height: 1;
    color: var(--brown);
  }
  .brand__dot {
    width: 12px; height: 12px;
    border-radius: 50%;
    background: var(--brown);
  }

  /* Loyalty side */
  .loyalty__brand { top: 48px; font-size: 34px; }
  .loyalty__stamps {
    position: absolute;
    top: 120px; left: 0; right: 0;
    display: flex;
    justify-content: center;
    gap: 16px;
  }
  .stamp {
    width: 56px; height: 56px;
    border-radius: 50%;
    border: 2px solid var(--brown);
    display: flex;
    align-items: center;
    justify-content: center;
    font-size: 13px;
    font-weight: 700;
  }
  .stamp--free { background: var(--brown); color: var(--gold); }
  .loyalty__offer {
    position: absolute;
    top: 212px; left: 0; right: 0;
    text-align: center;
    font-size: 17px;
  }

  /* Contact side */
  .contact__brand { top: 32px; font-size: 30px; }
  .contact__band {
    position: absolute;
    top: 88px; left: 0;
    width: 540px; height: 70px;
  }
  .contact__details {
    position: absolute;
    top: 172px; left: 0; right: 0;
    display: flex;
    flex-direction: column;
    align-items: center;
    gap: 7px;
    font-size: 12px;
  }
  .contact__address {
    font-family: "Amiri", serif;
    font-size: 13px;
    direction: rtl;
  }
  .contact__line { display: flex; align-items: center; gap: 6px; }
  .contact__icon { width: 12px; height: 12px; fill: var(--brown); }
  .contact__social { display: flex; align-items: center; gap: 10px; margin-top: 2px; }
  .social__handle { display: flex; align-items: center; gap: 4px; }
  .social__dot { width: 10px; height: 10px; border-radius: 50%; background: var(--brown); }
</style>
</head>
<body>

  <section class="card card--loyalty" aria-label="Loyalty card">
    <div class="card__corner card__corner--tl" role="img" aria-label="Corner flourish"></div>
    <div class="card__corner card__corner--tr" role="img" aria-label="Corner flourish"></div>
    <div class="card__corner card__corner--bl" role="img" aria-label="Corner flourish"></div>
    <div class="card__corner card__corner--br" role="img" aria-label="Corner flourish"></div>
    <div class="card__frame"></div>
    <p class="brand loyalty__brand"><span class="brand__dot"></span>Qamra</p>
    <div class="loyalty__stamps">
      <span class="stamp" role="img" aria-label="Stamp 1"></span>
      <span class="stamp" role="img" aria-label="Stamp 2"></span>
      <span class="stamp" role="img" aria-label="Stamp 3"></span>
      <span class="stamp" role="img" aria-label="Stamp 4"></span>
      <span class="stamp" role="img" aria-label="Stamp 5"></span>
      <span class="stamp stamp--free">FREE</span>
    </div>
    <p class="loyalty__offer">Buy 5 and get the 6th refill for free</p>
  </section>

  <section class="card card--contact" aria-label="Business card">
    <div class="card__corner card__corner--tl" role="img" aria-label="Corner flourish"></div>
    <div class="card__corner card__corner--tr" role="img" aria-label="Corner flourish"></div>
    <div class="card__corner card__corner--bl" role="img" aria-label="Corner flourish"></div>
    <div class="card__corner card__corner--br" role="img" aria-label="Corner flourish"></div>
    <div class="card__frame"></div>

    <p class="brand contact__brand"><span class="brand__dot"></span>Qamra</p>

    <svg class="contact__band" viewBox="0 0 540 70" role="img" aria-label="Brown wavy band with ornamental pattern">
      <path d="M0 14 C90 0 180 26 270 12 S450 0 540 14 L540 58 C450 70 360 46 270 58 S90 70 0 56 Z" fill="#5a2c22"/>
    </svg>

    <div class="contact__details">
      <p class="contact__address">الكويت، شارع السوق، مجمع النخيل، الدور الأول</p>
      <p class="contact__line">
        <svg class="contact__icon" viewBox="0 0 16 16"><path d="M1 3h14v10H1z M2 4l6 5 6-5" fill="none" stroke="#5a2c22" stroke-width="1.5"/></svg>
        QamraKuwait@qamramail.com
      </p>
      <p class="contact__line">
        <svg class="contact__icon" viewBox="0 0 16 16"><path d="M4 1l3 3-2 2c1 2 3 4 5 5l2-2 3 3-2 3C7 15 1 9 1 3z"/></svg>
        90041275
      </p>
      <div class="contact__social">
        <span>Follow us on :</span>
        <span class="social__handle"><span class="social__dot"></span>@Qamra</span>
        <span class="social__handle"><span class="social__dot"></span>@QamraKuwait</span>
      </div>
    </div>
  </section>

</body>
</html>
```